Brookfell Self Storage - Business Sign

The sign we are needing designed is our main road sign for our self-storage business. The dimensions of the sign are 57 inches tall x 96 inches wide. We require that our attached logo be on the sign as well as our phone number: 478-216-4387 and website www.BrookfellStorage.net. Optional information that can be added but not required is our address: 418 Marlow Tenney Pkwy, Centerville, GA 31047.

Industry/Entity Type

Self Storage

Font styles to use
Sans Serif

```html
<!DOCTYPE html>
<html lang="en">
<head>
<meta charset="utf-8">
<title>Brookfell Self Storage – Road Sign</title>
<link rel="stylesheet" href="https://fonts.googleapis.com/css2?family=Open+Sans:wght@600;700;800&display=swap">
<style>
  :root {
    --brand-blue: #4376bb;
    --photo-light: #6f9fd8;
    --photo-deep: #1f4fa8;
    --photo-grey: #8a9099;
    --ink: #3d3d3d;
    --ink-soft: #4a4a4a;
    --paper: #ffffff;
    --backdrop: #e6e6e6;
  }
  * { margin: 0; padding: 0; box-sizing: border-box; }
  html, body {
    width: 1200px;
    height: 920px;
    overflow: hidden;
    background: var(--backdrop);
    font-family: "Open Sans", Arial, sans-serif;
  }
  .sign {
    position: absolute;
    left: 30px;
    top: 121px;
    width: 1140px;
    height: 677px;
    background: var(--paper);
    overflow: hidden;
  }
  .sign-shapes {
    position: absolute;
    inset: 0;
    width: 100%;
    height: 100%;
  }
  .brand-band { fill: var(--brand-blue); }
  .address-bar { fill: var(--paper); }

  .brand-name {
    position: absolute;
    left: 80px;
    width: 640px;
    text-align: center;
    color: var(--ink-soft);
    font-weight: 700;
    line-height: 1;
  }
  .brand-name-main {
    top: 88px;
    font-size: 122px;
    letter-spacing: -1px;
  }
  .brand-name-sub {
    top: 254px;
    font-size: 54px;
    letter-spacing: 0.2em;
    padding-left: 0.2em;
  }

  .phone {
    position: absolute;
    left: 42px;
    top: 370px;
    font-size: 106px;
    font-weight: 800;
    color: var(--paper);
    line-height: 1;
    letter-spacing: -1px;
  }
  .website {
    position: absolute;
    left: 44px;
    top: 500px;
    font-size: 46px;
    font-weight: 700;
    color: var(--paper);
    line-height: 1;
  }
  .address {
    position: absolute;
    left: 46px;
    top: 616px;
    font-size: 29px;
    font-weight: 700;
    color: var(--ink);
    line-height: 1;
  }
</style>
</head>
<body>
  <main class="sign">
    <svg class="sign-shapes" viewBox="0 0 1140 677" xmlns="http://www.w3.org/2000/svg">
      <defs>
        <linearGradient id="facility-tones" x1="0" y1="0" x2="1" y2="1">
          <stop offset="0" stop-color="var(--photo-light)"/>
          <stop offset="0.45" stop-color="var(--photo-deep)"/>
          <stop offset="1" stop-color="var(--photo-grey)"/>
        </linearGradient>
      </defs>
      <path class="brand-band" d="M1075 0 H1140 V677 H0 V347 H640 Q725 347 790 284 Z"/>
      <path class="facility-photo" role="img" aria-label="Photo of a row of storage units with blue roll-up doors"
            fill="url(#facility-tones)"
            d="M1140 77 L792 425 Q768 449 790 476 L890 600 L1140 600 Z"/>
      <path class="address-bar" d="M0 592 H774 A40 40 0 0 1 814 632 V677 H0 Z"/>
    </svg>

    <div class="brand-name brand-name-main">Brookfell</div>
    <div class="brand-name brand-name-sub">SELF STORAGE</div>

    <p class="phone">478-216-4387</p>
    <p class="website">www.BrookfellStorage.net</p>
    <p class="address">418 Marlow Tenney Pkwy, Centerville, GA 31047</p>
  </main>
</body>
</html>
```